Brimovex business card

Based on company logo and website given , to design a business card temple. Slogan "Your furry friends deserves the best"
Color style please refer to our website

```html
<!DOCTYPE html>
<html lang="en">
<head>
<meta charset="utf-8">
<title>Brimovex business card</title>
<link rel="stylesheet" href="https://fonts.googleapis.com/css2?family=Crimson+Pro:wght@600;700&family=Montserrat:wght@700&family=Questrial&family=Mulish:wght@700&display=swap">
<style>
  :root {
    --olive: #bcae30;
    --olive-soft: #d7cc6e;
    --olive-pale: #efe9b8;
    --ink: #1d1d1d;
    --paper: #ffffff;
    --stage: #34454d;
  }
  * { box-sizing: border-box; margin: 0; padding: 0; }
  html, body { width: 1200px; height: 900px; overflow: hidden; }
  body { background: var(--stage); position: relative; }

  .card {
    position: absolute;
    left: 270px;
    width: 660px;
    height: 377px;
    background: var(--paper);
    overflow: hidden;
    box-shadow: 0 12px 30px rgba(0,0,0,.35);
  }
  .card--front { top: 45px; }
  .card--back  { top: 470px; }

  .brand-name {
    position: absolute;
    font-family: "Crimson Pro", serif;
    font-weight: 600;
    line-height: 1;
    letter-spacing: -0.01em;
    white-space: nowrap;
  }

  /* front */
  .front__band {
    position: absolute; top: 0; right: 0;
    width: 150px; height: 100%;
    background: var(--olive);
  }
  .front__art {
    position: absolute; left: 400px; top: 60px;
    width: 220px; height: 317px;
    border-radius: 110px 110px 0 0;
    background: linear-gradient(160deg, var(--olive-soft), var(--olive));
  }
  .front .brand-name { left: 110px; top: 78px; font-size: 58px; color: var(--olive); }
  .front__slogan {
    position: absolute; left: 56px; top: 148px;
    font-family: "Montserrat", sans-serif;
    font-weight: 700; font-size: 8.5px;
    letter-spacing: .28em; text-transform: uppercase;
    white-space: nowrap;
    color: var(--ink);
  }

  /* back */
  .back__panel {
    position: absolute; left: 0; top: 0;
    width: 240px; height: 100%;
    background: var(--olive);
  }
  .back__art {
    position: absolute; left: 150px; top: 120px;
    width: 240px; height: 257px;
    border-radius: 110px 110px 0 0;
    background: linear-gradient(200deg, var(--olive-pale), var(--olive-soft));
  }
  .back .brand-name { left: 30px; top: 46px; font-size: 46px; color: var(--paper); }

  .person { position: absolute; left: 410px; top: 26px; }
  .person__name {
    font-family: "Crimson Pro", serif; font-weight: 700;
    font-size: 32px; color: var(--olive); line-height: 1.1;
    white-space: nowrap;
  }
  .person__role {
    font-family: "Questrial", sans-serif; font-size: 11px;
    letter-spacing: .3em; color: var(--ink); text-transform: uppercase;
  }

  .contact-list {
    position: absolute; left: 470px; top: 170px;
    list-style: none;
  }
  .contact-item {
    display: flex; align-items: center; gap: 10px;
    height: 30px; margin-bottom: 2px;
    font-family: "Questrial", sans-serif; font-size: 13px; color: var(--ink);
    white-space: nowrap;
  }
  .contact-icon {
    width: 22px; height: 22px; border-radius: 50%;
    background: var(--olive);
    display: flex; align-items: center; justify-content: center;
  }
  .contact-icon svg { width: 12px; height: 12px; }

  .address-rule {
    position: absolute; left: 405px; right: 0; top: 290px;
    height: 2px; background: var(--olive);
  }
  .address {
    position: absolute; left: 405px; top: 300px;
    font-family: "Mulish", sans-serif; font-weight: 700;
    font-size: 13px; color: var(--olive);
    white-space: nowrap;
  }
</style>
</head>
<body>

<section class="card card--front front">
  <div class="front__band"></div>
  <div class="front__art" role="img" aria-label="Line illustration of a seated pet in olive outline"></div>
  <div class="brand-name">Brimovex</div>
  <p class="front__slogan">Your furry friends deserves the best</p>
</section>

<section class="card card--back back">
  <div class="back__panel"></div>
  <div class="back__art" role="img" aria-label="Line illustration of a seated pet in olive outline"></div>
  <div class="brand-name">Brimovex</div>

  <div class="person">
    <p class="person__name">Daniel Harper</p>
    <p class="person__role">Designation</p>
  </div>

  <ul class="contact-list">
    <li class="contact-item">
      <span class="contact-icon">
        <svg viewBox="0 0 24 24"><path fill="#fff" d="M6.6 10.8a15.5 15.5 0 0 0 6.6 6.6l2.2-2.2c.3-.3.7-.4 1-.2 1.1.4 2.300.6 3.6.6.6 0 1 .4 1 1V20c0 .6-.4 1-1 1A17 17 0 0 1 3 4c0-.6.4-1 1-1h3.5c.6 0 1 .4 1 1 0 1.3.2 2.5.6 3.6.1.3 0 .7-.2 1z"/></svg>
      </span>
      +61 3 5550 1928
    </li>
    <li class="contact-item">
      <span class="contact-icon">
        <svg viewBox="0 0 24 24"><rect x="3" y="6" width="18" height="12" fill="none" stroke="#fff" stroke-width="2"/><path d="M3 6l9 7 9-7" fill="none" stroke="#fff" stroke-width="2"/></svg>
      </span>
      hello@brimovex.com.au
    </li>
    <li class="contact-item">
      <span class="contact-icon">
        <svg viewBox="0 0 24 24" fill="none" stroke="#fff" stroke-width="2"><circle cx="12" cy="12" r="9"/><ellipse cx="12" cy="12" rx="4" ry="9"/><path d="M3 12h18"/></svg>
      </span>
      www.brimovex.com.au
    </li>
  </ul>

  <div class="address-rule"></div>
  <p class="address">4/22 Larkin Street, Glen Ashby Vic 3150</p>
</section>

</body>
</html>
```